Northern Falcon 250 Poster Design

Poster for the Public to draw them to the Event
- Northern Falcon 250. Largest Prize Money Race in Western Canada to Late Model Racing. Driver Competing for $65,000 in Prize Money Featuring Late Models and Street Stock Racers from Canada and the U.S. Don't miss the Inaugural Northern Falcon 250 at the Newly renovated Kellmore Raceway .
-Kellmore Raceway Address 4815 Dunvale Road
- April 29th -30th
- Gates Open and 4:30 pm Racing starts at 5 pm
- Adults $20
- Youth 12-17 $15
- Senior $15
- Under 12 Free

This is a major event and the newly renovated Kellmore Raceway that will attract racers from many cities and Kick off the 2022 racing Season

Target Market(s)

Fans

Industry/Entity Type

Autombobile race

Requirements
Must have
• Dates, times, logo, address, cars
Nice to have
• Clear bold Dates, draws the eyes, cool car pictures of Asphalt Late Model Race Cars

```html
<!DOCTYPE html>
<html lang="en">
<head>
<meta charset="utf-8">
<title>Northern Falcon 250 Poster</title>
<link href="https://fonts.googleapis.com/css2?family=Orbitron:wght@800;900&family=Montserrat:ital,wght@0,500;0,600;0,700;1,500;1,800&family=Oswald:wght@700&display=swap" rel="stylesheet">
<style>
  :root {
    --stage: #e0e0e0;
    --ink: #0b0b0b;
    --yellow: #f2c318;
    --white: #ffffff;
    --lime: #d6e63a;
    --orange: #f07a1e;
  }
  * { margin: 0; padding: 0; box-sizing: border-box; }
  html, body { width: 1200px; height: 1200px; overflow: hidden; background: var(--stage); }
  .poster {
    position: absolute; left: 212px; top: 52px; width: 775px; height: 1096px;
    background: linear-gradient(180deg, #3a3a3a 0%, #161616 18%, #0a0a0a 40%, #050505 100%);
    overflow: hidden; color: var(--white);
    font-family: "Montserrat", Arial, sans-serif;
  }
  .poster__rays { position: absolute; left: 0; top: 0; width: 775px; height: 420px; }
  .event-mark {
    position: absolute; top: 96px; left: 0; width: 100%;
    display: flex; justify-content: center; align-items: center; gap: 10px;
  }
  .event-mark__dot { width: 14px; height: 14px; border-radius: 50%; background: var(--yellow); }
  .event-mark__name { font-weight: 700; font-size: 22px; color: var(--white); letter-spacing: 1px; text-transform: uppercase; }
  .headline { position: absolute; left: 0; width: 100%; text-align: center; font-family: "Orbitron", Arial, sans-serif; font-weight: 900; line-height: 1; }
  .headline--top { top: 198px; font-size: 64px; color: var(--white); letter-spacing: 2px; }
  .headline--sub { top: 262px; font-size: 45px; color: var(--yellow); letter-spacing: 0.5px; }
  .tagline { position: absolute; top: 312px; left: 0; width: 100%; text-align: center; font-weight: 700; font-size: 16px; letter-spacing: 0.5px; }
  .hero {
    position: absolute; top: 340px; left: 0; width: 775px; height: 400px;
    background:
      radial-gradient(ellipse 30% 22% at 50% 30%, rgba(214,230,58,1) 0%, rgba(214,230,58,0.95) 55%, rgba(214,230,58,0) 100%),
      radial-gradient(ellipse 38% 22% at 50% 70%, rgba(240,240,240,1) 0%, rgba(225,225,225,0.95) 55%, rgba(225,225,225,0) 100%),
      radial-gradient(ellipse 36% 6% at 50% 88%, rgba(240,122,30,0.95) 0%, rgba(240,122,30,0) 100%),
      radial-gradient(ellipse 20% 26% at 10% 55%, rgba(30,34,60,0.95) 0%, rgba(30,34,60,0) 100%),
      radial-gradient(ellipse 20% 26% at 90% 55%, rgba(30,34,60,0.95) 0%, rgba(30,34,60,0) 100%),
      linear-gradient(180deg, #1a1a1a 0%, #262626 45%, #3d3d3d 80%, #2a2a2a 92%, #141414 100%);
  }
  .blurb {
    position: absolute; top: 760px; left: 60px; width: 655px; text-align: center;
    font-style: italic; font-weight: 500; font-size: 14px; line-height: 1.25;
  }
  .blurb strong { font-weight: 800; }
  .address {
    position: absolute; top: 829px; left: 0; width: 100%; text-align: center;
    font-family: "Orbitron", Arial, sans-serif; font-weight: 800; font-size: 13px; color: var(--yellow); letter-spacing: 0.5px;
  }
  .dates { position: absolute; top: 850px; left: 0; width: 100%; display: flex; justify-content: center; align-items: center; gap: 8px; }
  .dates__days { font-family: "Oswald", Arial, sans-serif; font-weight: 700; font-size: 46px; color: var(--yellow); line-height: 1; }
  .dates__month { font-weight: 700; font-size: 18px; line-height: 1; }
  .gates {
    position: absolute; top: 904px; left: 208px; width: 359px; height: 26px;
    border: 1px solid #8a8a8a; border-radius: 13px; background: #1e1e1e;
    text-align: center; font-weight: 600; font-size: 12.5px; line-height: 24px;
  }
  .divider { position: absolute; top: 944px; left: 100px; width: 575px; height: 1px; background: linear-gradient(90deg, transparent, #777, transparent); }
  .prices { position: absolute; top: 960px; left: 0; width: 775px; height: 100px; }
  .price-tag { font-weight: 700; fill: var(--ink); }
  .flag { position: absolute; left: 345px; top: 1004px; width: 92px; height: 36px; background: linear-gradient(135deg, #f2f2f2, #8a8a8a); transform: skewY(-10deg); }
</style>
</head>
<body>
<main class="poster">
  <svg class="poster__rays" viewBox="0 0 775 420" aria-hidden="true">
    <polygon points="0,0 775,0 775,30 520,420 255,420 0,38" fill="#262626"/>
    <polygon points="0,38 255,420 0,420" fill="#000"/>
    <polygon points="775,30 520,420 775,420" fill="#000"/>
  </svg>

  <div class="event-mark">
    <span class="event-mark__dot"></span>
    <span class="event-mark__name">Northern Falcon 250</span>
  </div>

  <h1 class="headline headline--top">LARGEST</h1>
  <h2 class="headline headline--sub">PRIZE MONEY RACE</h2>
  <p class="tagline">IN WESTERN CANADA TO LATE MODEL RACING</p>

  <div class="hero" role="img" aria-label="Three asphalt late model race cars on a checkered start line: a lime, white and orange car in front flanked by two dark navy cars, with a tire mark and falcon artwork above"></div>

  <p class="blurb">Driver Competing for <strong>$65,000 in Prize Money</strong> Featuring Late Models and Street Stock Racers from Canada and the U.S. Don't miss the Inaugural Northern Falcon 250 at the Newly renovated Kellmore Raceway .</p>

  <p class="address">KELLMORE RACEWAY ADDRESS 4815 DUNVALE ROAD</p>

  <div class="dates">
    <span class="dates__days">29TH -30TH</span>
    <span class="dates__month">APRIL<br>2022</span>
  </div>

  <p class="gates">Gates Open and 4:30 pm | Racing starts at 5 pm</p>
  <div class="divider"></div>

  <svg class="prices" viewBox="0 0 775 100" aria-hidden="true">
    <defs>
      <linearGradient id="barLeft" x1="0" x2="1"><stop offset="0" stop-color="#0a0a0a"/><stop offset="1" stop-color="#2a2a2a"/></linearGradient>
      <linearGradient id="barRight" x1="1" x2="0"><stop offset="0" stop-color="#0a0a0a"/><stop offset="1" stop-color="#2a2a2a"/></linearGradient>
    </defs>
    <polygon points="0,9 256,9 236,47 0,47" fill="url(#barLeft)"/>
    <polygon points="0,55 236,55 216,93 0,93" fill="url(#barLeft)"/>
    <polygon points="262,9 342,9 322,47 242,47" fill="var(--yellow)"/>
    <polygon points="242,55 322,55 302,93 222,93" fill="var(--yellow)"/>
    <polygon points="443,9 513,9 533,47 463,47" fill="var(--yellow)"/>
    <polygon points="463,55 533,55 553,93 483,93" fill="var(--yellow)"/>
    <polygon points="519,9 775,9 775,47 539,47" fill="url(#barRight)"/>
    <polygon points="539,55 775,55 775,93 559,93" fill="url(#barRight)"/>
    <text class="price-tag" x="292" y="35" text-anchor="middle" font-family="Montserrat, Arial, sans-serif" font-size="17">$20</text>
    <text class="price-tag" x="272" y="80" text-anchor="middle" font-family="Montserrat, Arial, sans-serif" font-size="17">$15</text>
    <text class="price-tag" x="488" y="35" text-anchor="middle" font-family="Montserrat, Arial, sans-serif" font-size="17">$15</text>
    <text class="price-tag" x="508" y="80" text-anchor="middle" font-family="Montserrat, Arial, sans-serif" font-size="12">12 FREE</text>
    <text x="210" y="33" text-anchor="end" fill="#fff" font-family="Montserrat, Arial, sans-serif" font-weight="600" font-size="15">ADULTS</text>
    <text x="210" y="79" text-anchor="end" fill="#fff" font-family="Montserrat, Arial, sans-serif" font-weight="600" font-size="15">YOUTH 12-17</text>
    <text x="566" y="33" fill="#fff" font-family="Montserrat, Arial, sans-serif" font-weight="600" font-size="15">SENIOR</text>
    <text x="566" y="79" fill="#fff" font-family="Montserrat, Arial, sans-serif" font-weight="600" font-size="15">UNDER</text>
  </svg>
  <div class="flag" role="img" aria-label="Waving checkered flag"></div>
</main>
</body>
</html>
```